KR Iron Designworks, Inc.

I'm looking for business card design for an existing company with an existing logo/website. www.kriron-designworks.example. VETERAN OWNED logo must be present.

Target Market(s)

Structural and architectural steel fabricators

Industry/Entity Type

Structural and architectural steel detailing and engineering

Contact Information for Business Card

logo, business name, address, phone, website, email, employee info

Font styles to use
Serif

Colors
00AB8E
00BBA5
67D7C9
C6EFE9
E9F9F6

Requirements
Must have
• company logo, website, VETERAN OWNED LOGO
Should not have
• Don't make it too busy. Less is more

```html
<!DOCTYPE html>
<html lang="en">
<head>
<meta charset="utf-8">
<title>KR Iron Designworks – Business Card</title>
<link rel="stylesheet" href="https://fonts.googleapis.com/css2?family=Open+Sans:wght@600&family=Roboto:ital,wght@0,400;0,700;1,400&display=swap">
<style>
  :root {
    --backdrop: #9b9c9e;
    --card-white: #ffffff;
    --slate: #31414d;
    --accent: #5ecbdc;
    --ink: #2b2b2b;
  }
  * { margin: 0; padding: 0; box-sizing: border-box; }
  html, body { width: 1200px; height: 1200px; overflow: hidden; }
  body { background: var(--backdrop); position: relative; font-family: "Roboto", sans-serif; }

  /* Front side */
  .card-front {
    position: absolute; left: 179px; top: 104px; width: 839px; height: 480px;
    background: var(--card-white); border-radius: 56px;
  }
  .card-front__panel {
    position: absolute; left: 35px; top: 36px; width: 768px; height: 408px;
    background: var(--slate); border-radius: 30px;
    display: flex; flex-direction: column; align-items: center;
  }
  .brand-name {
    font-family: "Open Sans", sans-serif; font-weight: 600;
    text-transform: uppercase; text-align: center; line-height: 1.15;
  }
  .card-front .brand-name {
    color: var(--card-white); font-size: 46px; letter-spacing: 2px; margin-top: 128px;
  }
  .card-front__web {
    color: var(--card-white); font-size: 18px; letter-spacing: 6.2px; margin-top: 68px;
  }

  /* Back side */
  .card-back {
    position: absolute; left: 179px; top: 604px; width: 839px; height: 480px;
    background: var(--card-white); border-radius: 56px; overflow: hidden;
  }
  .card-back__shapes { position: absolute; inset: 0; }
  .card-back .brand-name {
    position: absolute; left: 83px; top: 72px; color: var(--slate);
    font-size: 26px; text-align: left; letter-spacing: 0.5px;
  }
  .contact-line {
    position: absolute; left: 103px; color: var(--ink); font-size: 23px; line-height: 28px;
  }
  .contact-line--phone { left: 111px; top: 194px; }
  .contact-line--email { top: 256px; }
  .contact-line--web { top: 318px; }
  .contact-line--address { top: 369px; }

  .veteran-badge {
    position: absolute; left: 806px; top: 848px; width: 180px; text-align: center;
    color: var(--card-white); line-height: 1;
  }
  .veteran-badge__main { display: block; font-weight: 700; font-size: 37px; }
  .veteran-badge__sub { display: block; font-style: italic; font-size: 29px; margin-top: 6px; letter-spacing: 1px; }
</style>
</head>
<body>

<section class="card-front">
  <div class="card-front__panel">
    <div class="brand-name">KR Iron<br>Designworks</div>
    <div class="card-front__web">www.kriron-designworks.example</div>
  </div>
</section>

<section class="card-back">
  <svg class="card-back__shapes" width="839" height="480" viewBox="0 0 839 480">
    <polygon points="587,184 839,116 839,480 651,480" fill="var(--slate)"/>
    <g fill="var(--accent)">
      <path d="M0,226 L66,190 Q90,178 102,196 L0,258 Z"/>
      <path d="M0,288 L66,252 Q90,240 102,258 L0,320 Z"/>
      <path d="M0,350 L66,314 Q90,302 102,320 L0,382 Z"/>
      <path d="M0,414 L66,378 Q90,366 102,384 L0,446 Z"/>
    </g>
    <g fill="#ffffff" stroke="var(--slate)" stroke-width="2">
      <circle cx="78" cy="208" r="11"/>
      <circle cx="78" cy="270" r="11"/>
      <circle cx="78" cy="332" r="11"/>
      <circle cx="78" cy="398" r="11"/>
    </g>
    <g fill="none" stroke="var(--slate)" stroke-width="1.6">
      <!-- phone -->
      <rect x="74" y="202" width="8" height="12" rx="1.5"/>
      <!-- mail -->
      <rect x="72" y="266" width="12" height="9" rx="1"/>
      <path d="M72,267 L78,272 L84,267"/>
      <!-- globe -->
      <circle cx="78" cy="332" r="6"/>
      <path d="M72,332 H84 M78,326 V338"/>
      <!-- pin -->
      <path d="M78,405 C74,400 73,397 73,395 A5,5 0 0 1 83,395 C83,397 82,400 78,405 Z"/>
      <circle cx="78" cy="395" r="1.6"/>
    </g>
  </svg>

  <div class="brand-name">KR Iron Designworks</div>

  <div class="contact-line contact-line--phone">5550142987</div>
  <div class="contact-line contact-line--email">sales@kriron-designworks.example</div>
  <div class="contact-line contact-line--web">www.kriron-designworks.example</div>
  <div class="contact-line contact-line--address">KR Iron Designworks 1480 Harbor Point Blvd.,<br>ste 300 Bayport, FL 30123</div>
</section>

<div class="veteran-badge">
  <span class="veteran-badge__main">VETERAN</span>
  <span class="veteran-badge__sub">OWNED</span>
</div>

</body>
</html>
```